Mobile Recording Studio needs business cards

Open to seeing a creative design, but I want to emphasis my logo and minimize the name/title and company information. Possible a fully black background on card.

My company is a mobile sound recording studio. ok to include a my trailer (actual or cartoon) on the card. My initial thought is more straight forward, but a good design will win me over.

SPECS:
CMYK color mode
High (300ppi) raster effect.
cover bleed area
please deliver: Illustrator file with layers and a pdf at completion.

Name and info for the business card:

Dallin Perry
ADR Mixer

email: Dallin@MixVault.com

address:
248 - 5170 East Hollister
Vancouver, BC V5R 2J4

phone:
604.518.2093 office

website:
www.MixVault.com

FB: @MixVault

Instagram: @TheMixVault

Industry/Entity Type

Television Production

Contact Information for Business Card

Dallin Perry
ADR Mixer

email: Dallin@MixVault.com

address:
248 - 5170 East Hollister
Vancouver, BC V5R 2J4

phone:
604.518.2093 office

website:
www.MixVault.com

FB: @MixVault

Instagram: @TheMixVault

Colors

Designer to choose colors to be used in the design.

Requirements
Must have
• emphasis my logo and minimize the name/title and company information.
• SPECS:
• CMYK color mode
• High (300ppi) raster effect.
• cover bleed area
• please deliver: Illustrator file with layers and a pdf at completion.
Nice to have
• maybe include the following:
• all black background or black theme
• my work trailer (actual or cartoon) refer to Instagram: @TheMixVault

```html
<!DOCTYPE html>
<html lang="en">
<head>
<meta charset="utf-8">
<title>The Mix Vault – Business Card</title>
<link rel="stylesheet" href="https://fonts.googleapis.com/css2?family=Open+Sans:wght@600;700&family=Tinos:wght@400;700&display=swap">
<style>
  :root {
    --page: #f1f1f0;
    --card-dark: #333333;
    --panel-grey: #666666;
    --photo-dark: #1e1f21;
    --photo-mid: #3a3c40;
    --silver-mid: #b9bcc0;
    --red: #e0242b;
    --red-light: #f05a3c;
    --text-light: #ffffff;
    --text-dark: #1d1d1d;
  }
  * { margin: 0; padding: 0; box-sizing: border-box; }
  html, body { width: 1054px; height: 1200px; overflow: hidden; background: var(--page); }
  body { position: relative; font-family: "Open Sans", Arial, sans-serif; }

  .card { position: absolute; left: 77px; width: 898px; overflow: hidden; }
  .card-front { top: 69px; height: 512px; background: var(--card-dark); }
  .card-back { top: 609px; height: 514px; background: var(--panel-grey); }
  .card-art { position: absolute; inset: 0; width: 100%; height: 100%; }

  .brand-name {
    position: absolute; left: 0; right: 0; top: 200px;
    text-align: center;
    font-family: "Tinos", "Times New Roman", serif;
    font-weight: 700; font-size: 74px; letter-spacing: 2px;
    color: var(--silver-mid);
  }
  .front-web {
    position: absolute; left: 0; right: 0; top: 468px;
    display: flex; justify-content: center; align-items: center; gap: 12px;
    padding-left: 120px;
  }
  .front-web .url { font-weight: 700; font-size: 16px; letter-spacing: 1px; color: var(--text-light); margin: 0 8px; }
  .dot { display: block; border-radius: 50%; background: var(--text-light); }

  .photo-area {
    position: absolute; inset: 0;
    clip-path: polygon(0 0, 203px 0, 489px 514px, 0 514px);
    background: linear-gradient(160deg, var(--photo-mid) 0%, var(--photo-dark) 70%);
  }

  .person-name {
    position: absolute; right: 136px; top: 64px; white-space: nowrap;
    font-family: "Tinos", "Times New Roman", serif; font-weight: 700;
    font-size: 42px; letter-spacing: 3px; color: var(--text-light);
  }
  .person-title { position: absolute; right: 140px; top: 120px; font-weight: 700; font-size: 18px; color: var(--text-dark); }
  .contact-line {
    position: absolute; right: 140px; font-weight: 700; font-size: 19px;
    line-height: 26px; color: var(--text-light); text-align: right; white-space: nowrap;
  }
  .icon { position: absolute; left: 790px; width: 36px; height: 36px; }
</style>
</head>
<body>

<section class="card card-front" aria-label="Card front">
  <svg class="card-art" viewBox="0 0 898 512" aria-hidden="true">
    <defs>
      <linearGradient id="silver" x1="0" x2="1">
        <stop offset="0" stop-color="#6f7378"/>
        <stop offset=".35" stop-color="#f4f4f4"/>
        <stop offset=".6" stop-color="#9a9ea3"/>
        <stop offset="1" stop-color="#e8e8e8"/>
      </linearGradient>
    </defs>
    <path d="M0 95 Q450 170 898 0" fill="none" stroke="var(--red)" stroke-width="4"/>
    <path d="M0 100 Q450 240 898 55 L898 80 Q450 240 0 112 Z" fill="url(#silver)"/>
    <path d="M0 452 Q420 400 898 430 L898 443 Q420 418 0 478 Z" fill="url(#silver)"/>
    <path d="M0 512 Q420 420 898 450" fill="none" stroke="var(--red-light)" stroke-width="4"/>
  </svg>
  <div class="brand-name">The Mix Vault</div>
  <div class="front-web">
    <span class="dot" style="width:4px;height:4px"></span>
    <span class="dot" style="width:6px;height:6px"></span>
    <span class="dot" style="width:8px;height:8px"></span>
    <span class="dot" style="width:10px;height:10px"></span>
    <span class="dot" style="width:12px;height:12px"></span>
    <span class="dot" style="width:15px;height:15px"></span>
    <span class="url">www.MixVault.com</span>
    <span class="dot" style="width:15px;height:15px"></span>
    <span class="dot" style="width:12px;height:12px"></span>
    <span class="dot" style="width:10px;height:10px"></span>
    <span class="dot" style="width:8px;height:8px"></span>
    <span class="dot" style="width:6px;height:6px"></span>
    <span class="dot" style="width:4px;height:4px"></span>
  </div>
</section>

<section class="card card-back" aria-label="Card back">
  <svg class="card-art" viewBox="0 0 898 514" aria-hidden="true">
    <defs>
      <linearGradient id="silverBack" x1="0" x2="1">
        <stop offset="0" stop-color="#e9e9e9"/>
        <stop offset=".45" stop-color="#c3c6ca"/>
        <stop offset=".7" stop-color="#f4f4f4"/>
        <stop offset="1" stop-color="#a9adb2"/>
      </linearGradient>
    </defs>
    <path d="M420 432 Q620 420 898 450 L898 514 L420 514 Z" fill="url(#silverBack)"/>
    <path d="M420 424 Q620 412 898 442" fill="none" stroke="#2b2b2b" stroke-width="4"/>
  </svg>
  <div class="photo-area" role="img" aria-label="Photo of the mobile recording trailer parked outside a studio building"></div>

  <div class="person-name">DALLIN PERRY</div>
  <div class="person-title">ADR Mixer</div>

  <div class="contact-line" style="top:165px">248 - 5170 East Hollister<br>Vancouver, BC V5R 2J4</div>
  <div class="contact-line" style="top:237px">Dallin@MixVault.com</div>
  <div class="contact-line" style="top:286px">604.518.2093</div>
  <div class="contact-line" style="top:338px">www.MixVault.com</div>
  <div class="contact-line" style="top:380px">@TheMixVault</div>

  <svg class="icon" style="top:172px" viewBox="0 0 36 36" aria-hidden="true">
    <path d="M18 3 L34 17 H29 V33 H7 V17 H2 Z" fill="var(--text-dark)"/>
    <rect x="14" y="21" width="8" height="7" fill="var(--panel-grey)"/>
  </svg>
  <svg class="icon" style="top:234px" viewBox="0 0 36 36" aria-hidden="true">
    <rect x="3" y="8" width="30" height="21" fill="var(--text-dark)"/>
    <path d="M3 8 L18 20 L33 8 M3 29 L14 18 M33 29 L22 18" fill="none" stroke="var(--panel-grey)" stroke-width="1.5"/>
  </svg>
  <svg class="icon" style="top:282px" viewBox="0 0 36 36" aria-hidden="true">
    <rect x="10" y="1" width="16" height="34" rx="3" fill="none" stroke="var(--text-dark)" stroke-width="2.5"/>
    <line x1="14" y1="30" x2="22" y2="30" stroke="var(--text-dark)" stroke-width="2"/>
  </svg>
  <svg class="icon" style="top:332px" viewBox="0 0 36 36" aria-hidden="true">
    <g fill="none" stroke="var(--text-dark)" stroke-width="2">
      <circle cx="18" cy="18" r="15"/>
      <ellipse cx="18" cy="18" rx="7" ry="15"/>
      <line x1="3" y1="18" x2="33" y2="18"/>
      <line x1="5" y1="11" x2="31" y2="11"/>
      <line x1="5" y1="25" x2="31" y2="25"/>
      <line x1="18" y1="3" x2="18" y2="33"/>
    </g>
  </svg>
  <svg class="icon" style="top:375px" viewBox="0 0 36 36" aria-hidden="true">
    <rect x="7" y="7" width="22" height="22" fill="none" stroke="var(--text-dark)" stroke-width="3"/>
  </svg>
</section>

</body>
</html>
```